Corwin Ashdale Building Company, Inc.
Business Cards, Letterhead, Envelopes, Fax Cover
Professional
Miles T. Fenwick
PO Box 48217
Ashford Hills, NC 27599
miles@corwinashdale-example.com
www.corwinashdale-example.com
looking for a traditional style card, however nothing dated. same goes for the stationary. Something that is creative , but still shows professionalism and adaptable to the corporate environment. We don't want gloss cards. waiting on office and fax #'s. should have those in a day or two. As for the font, I put use same as logo font, but may want to see standard as well.
CA

```html
<!DOCTYPE html>
<html lang="en">
<head>
<meta charset="utf-8">
<title>Corwin Ashdale Building Company – Business Cards</title>
<link rel="stylesheet" href="https://fonts.googleapis.com/css2?family=Montserrat:wght@400;500;600&display=swap">
<style>
  :root {
    --backdrop: #2b2b2d;
    --card-white: #ffffff;
    --navy: #3c4a74;
    --ink-grey: #6f7278;
    --soft-grey: #e6e6e8;
  }
  * { margin: 0; padding: 0; box-sizing: border-box; }
  html, body { width: 1200px; height: 852px; overflow: hidden; }
  body {
    background: var(--backdrop);
    font-family: "Montserrat", Arial, sans-serif;
    position: relative;
  }
  .card {
    position: absolute;
    border-radius: 14px;
    box-shadow: 0 6px 18px rgba(0,0,0,0.35);
    overflow: hidden;
  }
  .card--back-peek { left: 300px; top: 232px; width: 120px; height: 130px; background: var(--navy); border-radius: 12px; }
  .card--front { left: 314px; top: 43px; width: 509px; height: 319px; background: var(--card-white); }
  .card--white-back { left: 602px; top: 396px; width: 554px; height: 317px; background: var(--card-white); }
  .card--navy-back { left: 34px; top: 473px; width: 619px; height: 312px; background: var(--navy); }

  .wordmark {
    position: absolute; left: 24px; top: 48px;
    display: flex; align-items: center; gap: 10px;
    color: var(--navy); font-weight: 500; font-size: 22px; letter-spacing: 0.5px;
    text-transform: uppercase;
  }
  .wordmark__square { width: 30px; height: 30px; background: var(--navy); }
  .wordmark__line2 {
    position: absolute; left: 64px; top: 80px;
    color: var(--navy); font-weight: 500; font-size: 12px; letter-spacing: 3px; text-transform: uppercase;
  }
  .person { position: absolute; left: 64px; top: 132px; }
  .person__name { color: var(--navy); font-weight: 500; font-size: 15px; letter-spacing: 1px; text-transform: uppercase; }
  .person__title { color: var(--ink-grey); font-size: 9px; letter-spacing: 1px; text-transform: uppercase; margin-top: 4px; }
  .contact {
    position: absolute; left: 64px; top: 192px;
    color: var(--ink-grey); font-size: 9px; line-height: 12.5px; letter-spacing: 0.6px; text-transform: uppercase;
    list-style: none;
  }
  .contact li:nth-child(3) { margin-top: 6px; }
  .faint-name {
    position: absolute; right: 18px; top: 170px;
    color: var(--soft-grey); font-weight: 600; font-size: 32px; line-height: 38px; text-align: right; text-transform: uppercase;
  }
  .center-name {
    position: absolute; inset: 0;
    display: flex; align-items: center; justify-content: center;
    font-weight: 600; font-size: 40px; letter-spacing: 1px; text-transform: uppercase;
  }
  .card--navy-back .center-name { color: var(--card-white); }
  .card--white-back .center-name { color: var(--navy); }
</style>
</head>
<body>
  <div class="card card--back-peek" aria-hidden="true"></div>

  <section class="card card--front" aria-label="Business card front">
    <div class="wordmark"><span class="wordmark__square"></span>Corwin Ashdale</div>
    <div class="wordmark__line2">Building Company</div>
    <div class="person">
      <p class="person__name">Miles T. Fenwick</p>
      <p class="person__title">Principal</p>
    </div>
    <ul class="contact">
      <li>PO Box 48217</li>
      <li>Ashford Hills, NC 27599</li>
      <li>P : 123-456-7890</li>
      <li>C : 919-555-0148</li>
      <li>F : 123-456-7890</li>
      <li>E : miles@corwinashdale-example.com</li>
      <li>W : www.corwinashdale-example.com</li>
    </ul>
    <div class="faint-name">Corwin<br>Ashdale</div>
  </section>

  <section class="card card--white-back" aria-label="Business card back, white">
    <div class="center-name">Corwin Ashdale</div>
  </section>

  <section class="card card--navy-back" aria-label="Business card back, navy">
    <div class="center-name">Corwin Ashdale</div>
  </section>
</body>
</html>
```